Business Card Design - Corporate

Create a sleek elegant business card layout while suggesting a color scheme. Convey cutting edge technology while maintaining a corporate feel that is easily readable.

Company designs and manufactures consumer electronic products for mass retail that are mainly app driven.

(vector logo and die-line provided)

Target Market(s)

Corporate level, tech industry.

Industry/Entity Type

Business

Contact Information for Business Card

Generic Info:

Name
Title
email
address
phone 1
phone 2
website (quillbarn.com) on back

Font styles to use
Sans Serif

Requirements
Must have
• At least 2 colors + white on one side.
Nice to have
• Solid suggestion on color for logo and overall design. Color flood on back of card.
Should not have
• background texture like... marble, stone, patterns or circuit boards

```html
<!DOCTYPE html>
<html lang="en">
<head>
<meta charset="utf-8">
<title>Quillbarn Business Card</title>
<link href="https://fonts.googleapis.com/css2?family=Open+Sans:wght@400;600;700&display=swap" rel="stylesheet">
<style>
  :root {
    --backdrop: #5a4a3b;
    --card-white: #ffffff;
    --ink-grey: #555557;
    --band-grey: #59595b;
    --flood-grey: #5c5c5e;
    --accent-blue: #1b6db4;
    --white: #ffffff;
  }
  * { margin: 0; padding: 0; box-sizing: border-box; }
  html, body {
    width: 1200px; height: 987px; overflow: hidden;
    background: var(--backdrop);
    font-family: "Open Sans", Arial, sans-serif;
  }
  .card {
    position: absolute; left: 293px; width: 615px; height: 352px;
    box-shadow: 0 2px 4px rgba(0,0,0,0.35);
  }
  .card--front { top: 130px; background: var(--card-white); }
  .card--back { top: 505px; background: var(--flood-grey); }

  .wordmark {
    position: absolute; left: 0; width: 100%; text-align: center;
    font-weight: 400; font-size: 54px; letter-spacing: 7px; line-height: 1;
  }
  .card--front .wordmark { top: 57px; color: var(--ink-grey); }
  .card--back .wordmark { top: 150px; color: var(--white); }

  .name-band {
    position: absolute; left: 0; top: 173px; width: 100%; height: 54px;
    background: var(--band-grey);
  }
  .name-band__name {
    position: absolute; right: 355px; top: 13px;
    color: var(--white); font-weight: 700; font-size: 20px; letter-spacing: 0.3px;
  }
  .name-band__title {
    position: absolute; left: 354px; top: 17px;
    color: var(--white); font-size: 15.5px;
  }
  .name-band__mark {
    position: absolute; left: 278px; top: -3px; width: 60px; height: 60px;
    border-radius: 50%; background: var(--white);
    border: 5px solid var(--accent-blue);
  }

  .contact {
    position: absolute; top: 256px; font-size: 15.5px; color: var(--ink-grey);
    line-height: 23.5px;
  }
  .contact--left { left: 40px; }
  .contact--right { right: 40px; text-align: right; }
  .contact__row { display: flex; align-items: center; gap: 6px; }
  .contact__icon { width: 15px; height: 15px; fill: var(--accent-blue); flex: none; }

  .back-pattern {
    position: absolute; inset: 0;
    background: radial-gradient(circle at 50% 50%, #626264 0%, var(--flood-grey) 70%);
  }
  .back-url {
    position: absolute; left: 0; top: 292px; width: 100%; text-align: center;
    color: var(--white); font-size: 15px; letter-spacing: 6px;
  }
</style>
</head>
<body>
  <section class="card card--front">
    <div class="wordmark">QUILLBARN</div>
    <div class="name-band">
      <span class="name-band__name">MARCUS HALE</span>
      <span class="name-band__mark"></span>
      <span class="name-band__title">CEO&amp;Founder</span>
    </div>
    <div class="contact contact--left">
      <div class="contact__row">
        <svg class="contact__icon" viewBox="0 0 24 24"><path d="M6.6 10.8c1.4 2.8 3.8 5.1 6.6 6.6l2.2-2.2c.3-.3.7-.4 1-.2 1.1.4 2.3.6 3.6.6.6 0 1 .4 1 1V20c0 .6-.4 1-1 1C10.6 21 3 13.4 3 4c0-.6.4-1 1-1h3.5c.6 0 1 .4 1 1 0 1.3.2 2.5.6 3.6.1.3 0 .7-.2 1z"/></svg>
        <span>555 210 4836</span>
      </div>
      <div class="contact__row">
        <svg class="contact__icon" viewBox="0 0 24 24"><path d="M6.6 10.8c1.4 2.8 3.8 5.1 6.6 6.6l2.2-2.2c.3-.3.7-.4 1-.2 1.1.4 2.3.6 3.6.6.6 0 1 .4 1 1V20c0 .6-.4 1-1 1C10.6 21 3 13.4 3 4c0-.6.4-1 1-1h3.5c.6 0 1 .4 1 1 0 1.3.2 2.5.6 3.6.1.3 0 .7-.2 1z"/></svg>
        <span>555 374 9162</span>
      </div>
      <div class="contact__row">
        <svg class="contact__icon" viewBox="0 0 24 24"><path d="M2 6h20v12H2z M2 6l10 7 10-7" fill="var(--accent-blue)" stroke="#fff" stroke-width="1.5"/></svg>
        <span>marcus@quillbarn.com</span>
      </div>
    </div>
    <div class="contact contact--right">
      <div>4120 Birchwood Court</div>
      <div>Juneau, Alaska 99801</div>
      <div>www.quillbarn.com</div>
    </div>
  </section>

  <section class="card card--back">
    <div class="back-pattern" role="img" aria-label="Repeating pattern of the brand symbol in soft grey tones"></div>
    <div class="wordmark">QUILLBARN</div>
    <div class="back-url">www.quillbarn.com</div>
  </section>
</body>
</html>
```